Horticulture Consulting Company Premium Card

We are looking for new design for a premium business card.
Our cards will be printed on glossy and embossed premium card stock.

Target Market(s)

Horticulture business owners needing our consulting services

Contact Information for Business Card

Marcus Thorne
(555) 348-2916
Marcus@velturaq.com

Requirements
Must have
• Company Logo and Contact information.
• Some additional work to add interest to the card
Should not have
• Red or Yellow

```html
<!DOCTYPE html>
<html lang="en">
<head>
<meta charset="utf-8">
<title>Veltura Horticulture – Business Card</title>
<link href="https://fonts.googleapis.com/css2?family=Oswald:wght@500&family=Lato:wght@400;700&display=swap" rel="stylesheet">
<style>
  :root {
    --bg: #e6e7e9;
    --card: #ffffff;
    --blue: #2d74b8;
    --green: #35a645;
    --ink: #222326;
  }
  html, body {
    margin: 0;
    width: 1200px;
    height: 1200px;
    overflow: hidden;
    background: var(--bg);
  }
  .stage {
    width: 1200px;
    height: 1200px;
    display: flex;
    align-items: center;
    justify-content: center;
  }
  .card {
    position: relative;
    width: 1000px;
    height: 572px;
    background: var(--card);
    box-shadow: 0 10px 30px rgba(0,0,0,0.15);
    overflow: hidden;
  }
  .brand {
    position: absolute;
    left: 70px;
    top: 250px;
    width: 380px;
    display: flex;
    align-items: center;
    gap: 14px;
  }
  .brand-mark {
    flex: 0 0 34px;
    height: 34px;
    border-radius: 50%;
    background: var(--green);
  }
  .brand-name {
    font-family: "Lato", sans-serif;
    font-weight: 700;
    font-size: 30px;
    line-height: 1;
    color: var(--blue);
    white-space: nowrap;
  }
  .person {
    position: absolute;
    left: 560px;
    top: 90px;
  }
  .person-name {
    font-family: "Oswald", sans-serif;
    font-weight: 500;
    font-size: 58px;
    line-height: 1;
    color: var(--blue);
    text-transform: uppercase;
    margin: 0;
  }
  .person-title {
    font-family: "Lato", sans-serif;
    font-size: 22px;
    color: var(--ink);
    letter-spacing: 1px;
    margin: 4px 0 22px;
  }
  .contact {
    list-style: none;
    margin: 0;
    padding: 0 0 0 50px;
    font-family: "Lato", sans-serif;
    font-size: 24px;
    color: var(--ink);
  }
  .contact li {
    display: flex;
    align-items: center;
    gap: 12px;
    margin-bottom: 8px;
  }
  .contact svg { width: 20px; height: 20px; fill: var(--green); }
  .band {
    position: absolute;
    left: 0;
    bottom: 0;
    width: 100%;
    height: 34px;
    display: flex;
    gap: 6px;
  }
  .band-blue { flex: 0 0 46%; background: var(--blue); }
  .band-green { flex: 1; background: var(--green); }
</style>
</head>
<body>
<div class="stage">
  <div class="card">
    <div class="brand">
      <div class="brand-mark"></div>
      <div class="brand-name">Veltura Horticulture</div>
    </div>

    <div class="person">
      <h1 class="person-name">Marcus Thorne</h1>
      <div class="person-title">MANAGER</div>
      <ul class="contact">
        <li>
          <svg viewBox="0 0 24 24" aria-hidden="true"><path d="M6.6 10.8a15.1 15.1 0 0 0 6.6 6.6l2.2-2.2a1 1 0 0 1 1-.25 11.4 11.4 0 0 0 3.6.57 1 1 0 0 1 1 1V20a1 1 0 0 1-1 1A17 17 0 0 1 3 4a1 1 0 0 1 1-1h3.5a1 1 0 0 1 1 1c0 1.25.2 2.45.57 3.57a1 1 0 0 1-.25 1z"/></svg>
          <span>(555) 348-2916</span>
        </li>
        <li>
          <svg viewBox="0 0 24 24" aria-hidden="true"><path d="M2 5h20v14H2z M2 5l10 8 10-8" stroke="#fff" stroke-width="1.5"/></svg>
          <span>Marcus@velturaq.com</span>
        </li>
      </ul>
    </div>

    <div class="band">
      <div class="band-blue"></div>
      <div class="band-green"></div>
    </div>
  </div>
</div>
</body>
</html>
```